Stationery Design Project

We are looking stationary Design for Velbrin Global, a high end clothing company. I have attached an image of our Logo below.
Updates
I am looking for designs for the following stationaries:
1. Leather Binders
2. Paper Binders
3. Letterhead
4. Envelopes
5. Pens, pencils etc
We would love to see designs with gold, black and white color combination.
Industry/Entity Type
Clothing
Look and feel
Each slider illustrates characteristics of the customer's brand and the style your logo design should communicate.

```html
<!DOCTYPE html>
<html lang="en">
<head>
<meta charset="utf-8">
<title>Velbrin Global — Stationery</title>
<link href="https://fonts.googleapis.com/css2?family=Playfair+Display:wght@700&family=Montserrat:wght@400;500;600&display=swap" rel="stylesheet">
<style>
  :root{
    --backdrop:#a9abb5;
    --ink:#2f333c;
    --ink-deep:#272a32;
    --pocket:#32363f;
    --gold:#c9974a;
    --gold-soft:#d6a85c;
    --paper:#fbfcff;
    --text-dark:#3a3d44;
    --watermark:#e9ebf1;
  }
  *{box-sizing:border-box;margin:0;padding:0}
  html,body{width:1200px;height:999px;overflow:hidden}
  body{background:var(--backdrop);position:relative;font-family:"Montserrat",Arial,sans-serif}
  .brand-name{font-family:"Playfair Display",Georgia,serif;font-weight:700;letter-spacing:.12em;text-transform:uppercase;white-space:nowrap}
  .brand-dot{border-radius:50%;border:1.5px solid currentColor}

  /* folder cover */
  .folder-cover{position:absolute;left:40px;top:236px;width:360px;height:527px;background:var(--ink);box-shadow:0 2px 6px rgba(0,0,0,.25)}
  .folder-cover .brand{position:absolute;left:0;right:0;top:80px;display:flex;flex-direction:column;align-items:center;color:var(--gold)}
  .folder-cover .brand-dot{width:58px;height:58px;margin-bottom:22px}
  .folder-cover .brand-name{font-size:20px}
  .folder-cover .foot-rule{position:absolute;left:118px;width:124px;bottom:62px;height:2px;background:var(--gold)}

  /* folder inside */
  .folder-inside{position:absolute;left:420px;top:236px;width:360px;height:527px;background:var(--ink-deep);box-shadow:0 2px 6px rgba(0,0,0,.25)}
  .folder-inside .pocket{position:absolute;left:0;right:0;bottom:0;height:205px;background:var(--pocket);border-top:1px solid #3c414b}
  .folder-inside .card-slot{position:absolute;right:52px;width:30px;height:30px;border-radius:50%;background:var(--ink-deep)}
  .folder-inside .card-slot.top{top:26px}
  .folder-inside .card-slot.bottom{bottom:10px;height:15px;border-radius:15px 15px 0 0}
  .contact-block{position:absolute;left:26px;top:70px;color:var(--gold-soft);font-size:8.5px;line-height:14px}
  .contact-block li{list-style:none;display:flex;align-items:center;gap:6px}
  .contact-block address{font-style:normal;margin-top:10px;line-height:13px}
  .icon{width:9px;height:9px;flex:none}

  /* letterhead */
  .letterhead{position:absolute;left:800px;top:160px;width:360px;height:509px;background:var(--paper);box-shadow:0 2px 6px rgba(0,0,0,.2)}
  .letterhead .brand{position:absolute;left:0;right:0;top:30px;display:flex;flex-direction:column;align-items:center;color:var(--text-dark)}
  .letterhead .brand-dot{width:30px;height:30px;margin-bottom:12px}
  .letterhead .brand-name{font-size:15px}
  .letterhead .watermark{position:absolute;left:90px;top:170px;width:180px;height:180px;border-radius:50%;background:radial-gradient(circle,var(--watermark) 0%,#f3f4f8 70%,transparent 71%)}
  .letterhead .footer{position:absolute;left:28px;right:28px;bottom:34px;display:flex;justify-content:space-between;font-size:5.6px;color:var(--text-dark);padding-bottom:7px;border-bottom:1.2px solid #222}
  .letterhead .footer span{display:flex;align-items:center;gap:3px}
  .letterhead .icon{width:6px;height:6px}

  /* business cards */
  .card{position:absolute;top:700px;width:170px;height:97px;box-shadow:0 2px 5px rgba(0,0,0,.2)}
  .card-front{left:800px;background:var(--paper);display:flex;align-items:center;color:var(--text-dark)}
  .card-front .brand{width:78px;display:flex;flex-direction:column;align-items:center}
  .card-front .brand-dot{width:16px;height:16px;margin-bottom:6px}
  .card-front .brand-name{font-size:6.4px;letter-spacing:.08em}
  .card-front .divider{width:1px;height:54px;background:#d5d7dd}
  .card-front .details{padding-left:9px;font-size:4.6px;line-height:7px}
  .card-front .person{font-weight:600;font-size:6px;letter-spacing:.04em}
  .card-front .role{color:#888;margin-bottom:4px}
  .card-back{left:990px;background:var(--ink);display:flex;flex-direction:column;align-items:center;justify-content:center;color:var(--gold)}
  .card-back .brand-dot{width:20px;height:20px;margin-bottom:8px}
  .card-back .brand-name{font-size:9px}
</style>
</head>
<body>
<svg width="0" height="0" style="position:absolute" aria-hidden="true">
  <defs>
    <symbol id="i-phone" viewBox="0 0 10 10"><circle cx="5" cy="5" r="4.4" fill="none" stroke="currentColor" stroke-width=".9"/><path d="M3.4 2.9l1 .1.4 1.1-.6.5a3 3 0 001.3 1.3l.5-.6 1.1.4.1 1c-2 .3-4.2-1.8-3.8-3.8z" fill="currentColor"/></symbol>
    <symbol id="i-mail" viewBox="0 0 10 10"><circle cx="5" cy="5" r="4.4" fill="none" stroke="currentColor" stroke-width=".9"/><rect x="2.8" y="3.5" width="4.4" height="3" fill="none" stroke="currentColor" stroke-width=".7"/><path d="M2.8 3.5L5 5.2l2.2-1.7" fill="none" stroke="currentColor" stroke-width=".7"/></symbol>
    <symbol id="i-web" viewBox="0 0 10 10"><circle cx="5" cy="5" r="4.4" fill="none" stroke="currentColor" stroke-width=".9"/><circle cx="5" cy="5" r="2.3" fill="none" stroke="currentColor" stroke-width=".7"/><path d="M2.7 5h4.6M5 2.7c-1 1.4-1 3.2 0 4.6M5 2.7c1 1.4 1 3.2 0 4.6" fill="none" stroke="currentColor" stroke-width=".5"/></symbol>
  </defs>
</svg>

<section class="folder-cover" aria-label="Presentation folder, front cover">
  <div class="brand"><span class="brand-dot"></span><span class="brand-name">Velbrin Global</span></div>
  <div class="foot-rule"></div>
</section>

<section class="folder-inside" aria-label="Presentation folder, inside pocket">
  <div class="pocket">
    <span class="card-slot top"></span>
    <span class="card-slot bottom"></span>
    <div class="contact-block">
      <ul>
        <li><svg class="icon"><use href="#i-phone"/></svg>(555) 014-2290</li>
        <li><svg class="icon"><use href="#i-mail"/></svg>info@velbringlobal.com</li>
        <li><svg class="icon"><use href="#i-web"/></svg>www.velbringlobal.com</li>
      </ul>
      <address>72 Harrow Lane<br>Westbrook, CA 90210</address>
    </div>
  </div>
</section>

<section class="letterhead" aria-label="Letterhead">
  <div class="brand"><span class="brand-dot"></span><span class="brand-name">Velbrin Global</span></div>
  <div class="watermark" role="img" aria-label="Faint brand emblem watermark"></div>
  <div class="footer">
    <span>72 Harrow Lane, Westbrook, CA 90210</span>
    <span><svg class="icon"><use href="#i-phone"/></svg>(555) 014-2290</span>
    <span><svg class="icon"><use href="#i-mail"/></svg>info@velbringlobal.com</span>
    <span><svg class="icon"><use href="#i-web"/></svg>www.velbringlobal.com</span>
  </div>
</section>

<section class="card card-front" aria-label="Business card, front">
  <div class="brand"><span class="brand-dot"></span><span class="brand-name">Velbrin Global</span></div>
  <div class="divider"></div>
  <div class="details">
    <div class="person">MARA LINDQVIST</div>
    <div class="role">Manager</div>
    <div>(555) 014-2291</div>
    <div>(555) 014-2290</div>
    <div>info@velbringlobal.com</div>
    <div>www.velbringlobal.com</div>
    <div style="margin-top:3px">72 Harrow Lane</div>
    <div>Westbrook, CA 90210</div>
  </div>
</section>

<section class="card card-back" aria-label="Business card, back">
  <span class="brand-dot"></span><span class="brand-name">Velbrin Global</span>
</section>
</body>
</html>
```